RTM Global (Rooted Tillage and Meadowcraft) is a company positioning itself as a global leader in regenerative and sustainable agriculture and irrigation technologies and solutions, with a focus on soil health. Please read the attached information (which can be used in the website).
We're looking for a modern website which also compliments the agricultural sector and the natural resources we work with. We want the website to be fairly concise and to the point without elaborating too much. We would rather attract the clients to engage with us rather than drawing their own conclusions from the website.

```html
<!DOCTYPE html>
<html lang="en">
<head>
<meta charset="utf-8">
<title>RTM Global — Rooted Tillage and Meadowcraft</title>
<link href="https://fonts.googleapis.com/css2?family=Lato:ital,wght@0,300;0,400;0,700;1,300&family=Open+Sans:wght@600&display=swap" rel="stylesheet">
<style>
  :root {
    --olive: #8a9170;
    --olive-btn: #878f6c;
    --blue: #3e5f8f;
    --ink: #2f2f2f;
    --muted: #555;
    --mist: #f7f7f7;
    --footer: #3a4620;
    --white: #ffffff;
  }
  * { margin: 0; padding: 0; box-sizing: border-box; }
  html, body { width: 1200px; height: 2886px; overflow: hidden; }
  body { position: relative; background: var(--white); font-family: 'Lato', sans-serif; color: var(--ink); }
  .abs { position: absolute; }

  /* Header */
  .site-header { position: absolute; top: 0; left: 0; width: 1200px; height: 75px; background: var(--white); border-bottom: 1px solid #ddd; z-index: 3; }
  .brand { position: absolute; left: 150px; top: 22px; display: flex; align-items: center; gap: 10px; }
  .brand-mark { width: 22px; height: 22px; background: var(--blue); }
  .brand-name { font-weight: 700; font-size: 26px; color: var(--blue); }
  .main-nav a { position: absolute; top: 30px; font-size: 12px; color: #555; text-decoration: none; text-transform: uppercase; letter-spacing: .2px; }
  .main-nav a.active { color: var(--olive); }
  .cta-solutions { position: absolute; left: 900px; top: 22px; width: 150px; height: 30px; background: var(--olive-btn); color: var(--white); font-size: 12px; font-weight: 700; display: flex; align-items: center; justify-content: center; border-radius: 2px; }

  /* Hero */
  .hero { position: absolute; top: 75px; left: 0; width: 1200px; height: 525px; overflow: hidden; }
  .hero-photo { position: absolute; inset: 0; background: linear-gradient(180deg, #2e3a22 0%, #46552c 35%, #3a4222 60%, #2d2418 100%); }
  .hero-title { position: absolute; top: 132px; width: 1200px; text-align: center; color: var(--white); font-family: 'Open Sans', sans-serif; font-weight: 600; font-size: 41px; letter-spacing: 2.5px; }
  .hero-sub { position: absolute; top: 195px; width: 1200px; text-align: center; color: var(--white); font-weight: 700; font-size: 30px; }
  .hero-tags { position: absolute; top: 248px; width: 1200px; text-align: center; color: var(--white); font-weight: 700; font-size: 19px; }
  .hero-btn { position: absolute; left: 495px; top: 317px; width: 225px; height: 45px; background: var(--olive-btn); color: var(--white); border-radius: 5px; display: flex; align-items: center; justify-content: center; font-family: 'Open Sans', sans-serif; font-weight: 600; font-size: 18px; letter-spacing: 1.5px; }
  .hero-wave { position: absolute; left: 0; bottom: 0; }

  /* Section headings */
  .section-heading { position: absolute; left: 0; width: 1200px; text-align: center; color: var(--olive); font-weight: 700; text-transform: uppercase; font-size: 37px; }
  .section-heading span { display: inline-block; border-bottom: 5px solid var(--blue); padding: 0 4px 0; line-height: 1.1; }

  /* Cards */
  .card { position: absolute; top: 772px; height: 354px; background: #f4f4f4; box-shadow: 0 1px 3px rgba(0,0,0,.18); text-align: center; }
  .card-icon { position: absolute; top: 34px; left: 50%; width: 110px; height: 110px; margin-left: -55px; border-radius: 50%; background: radial-gradient(circle, rgba(70,130,190,.22), rgba(138,145,112,.12)); }
  .card-title { position: absolute; top: 163px; left: 10px; right: 10px; font-size: 17px; line-height: 24px; color: var(--ink); }
  .card-text { position: absolute; left: 13px; right: 13px; font-size: 12px; line-height: 18px; color: var(--muted); text-align: justify; text-align-last: center; }

  /* Mission */
  .mission { position: absolute; top: 1202px; left: 0; width: 1200px; height: 652px; background: var(--mist); }
  .mission-text { position: absolute; left: 152px; width: 885px; top: 1467px; font-weight: 300; font-style: italic; font-size: 29px; line-height: 40.5px; color: #444; text-align: justify; text-align-last: center; }
  .mission-text em { color: var(--blue); font-style: italic; }

  /* Why */
  .why-photo { position: absolute; left: 0; top: 1952px; width: 561px; height: 479px; background: linear-gradient(160deg, #2c3550 0%, #6a5540 40%, #876b4e 70%, #5f4a35 100%); }
  .why-box { position: absolute; left: 561px; top: 1927px; width: 488px; height: 524px; border: 4px solid var(--blue); background: var(--white); }
  .why-title { position: absolute; left: 32px; top: 14px; width: 246px; white-space: nowrap; font-size: 35px; line-height: 44px; color: var(--olive); font-weight: 400; padding-bottom: 6px; border-bottom: 5px solid var(--blue); }
  .why-list { list-style: none; }
  .why-item { position: absolute; left: 32px; width: 412px; font-size: 16.5px; line-height: 27px; color: #444; padding-left: 36px; }
  .why-item .num { position: absolute; left: 0; top: -3px; font-size: 21px; font-weight: 700; color: var(--blue); }
  .why-item strong { font-weight: 400; color: var(--blue); }

  /* Impact */
  .impact { position: absolute; top: 2526px; left: 0; width: 1200px; height: 270px; background: linear-gradient(135deg, #a8803c 0%, #c9a664 35%, #b48d48 65%, #8e6a2e 100%); }
  .impact-title { position: absolute; top: 55px; width: 1200px; text-align: center; color: var(--white); font-weight: 700; font-size: 36px; }
  .impact-text { position: absolute; left: 216px; width: 840px; top: 140px; color: var(--white); font-size: 22px; line-height: 27px; }

  /* Footer */
  .site-footer { position: absolute; top: 2841px; left: 0; width: 1200px; height: 45px; background: var(--footer); }
  .copyright { position: absolute; left: 151px; top: 16px; font-size: 11px; color: var(--white); }
  .social { position: absolute; top: 9px; width: 27px; height: 27px; border: 1.5px solid var(--white); border-radius: 50%; }
</style>
</head>
<body>

<header class="site-header">
  <div class="brand"><span class="brand-mark"></span><span class="brand-name">RTM Global</span></div>
  <nav class="main-nav">
    <a class="active" style="left:390px">Home</a>
    <a style="left:453px">Our Mission</a>
    <a style="left:559px">Our Products</a>
    <a style="left:679px">Our Services</a>
    <a style="left:789px">Our Impact</a>
  </nav>
  <div class="cta-solutions">Discover Our Solutions</div>
</header>

<section class="hero">
  <div class="hero-photo" role="img" aria-label="Farmer walking between rows of young crops in a field at sunset"></div>
  <h1 class="hero-title">Rooted Tillage and Meadowcraft (RTM)</h1>
  <p class="hero-sub">Revolutionizing Agriculture with Regenerative Solutions</p>
  <p class="hero-tags">Mobile Drip Irrigation | Agronomy | Soil Health | Regenerative Technologies</p>
  <div class="hero-btn">Explore Our Impact</div>
  <svg class="hero-wave" width="1200" height="70" viewBox="0 0 1200 70" aria-hidden="true">
    <path d="M0 28 C 200 75, 420 70, 700 50 C 900 36, 1080 8, 1200 20 L1200 70 L0 70 Z" fill="#ffffff"/>
  </svg>
</section>

<h2 class="section-heading" style="top:668px"><span>Our Core Products and Services</span></h2>

<article class="card" style="left:150px;width:214px">
  <div class="card-icon" role="img" aria-label="Icon of a hand holding a seedling"></div>
  <h3 class="card-title">Regenerative Agricultural Technologies</h3>
  <p class="card-text" style="top:230px">Unlock the future of farming with the latest practices and tools designed to rebuild ecosystems, improve biodiversity, and restore soil carbon levels.</p>
</article>
<article class="card" style="left:375px;width:214px">
  <div class="card-icon" role="img" aria-label="Icon of drip irrigation watering seedlings"></div>
  <h3 class="card-title">Mobile Drip Irrigation</h3>
  <p class="card-text" style="top:228px">Our advanced irrigation system maximizes water use effciency, reduces waste, and promotes healthier crops.</p>
</article>
<article class="card" style="left:605px;width:215px">
  <div class="card-icon" role="img" aria-label="Icon of a globe with leaves"></div>
  <h3 class="card-title">Soil Health Solutions</h3>
  <p class="card-text" style="top:228px;line-height:24px">From analysis to rehabilitation, we help you restore soil fertility, improve water retention, and reduce dependency on chemical inputs.</p>
</article>
<article class="card" style="left:836px;width:214px">
  <div class="card-icon" role="img" aria-label="Icon of a gear with growing plants"></div>
  <h3 class="card-title">Agronomy Services</h3>
  <p class="card-text" style="top:228px">Expert advice and customized crop management plans to boost productivity while supporting regenerative outcomes.</p>
</article>

<section class="mission">
  <svg class="abs" style="left:0;bottom:0" width="1200" height="70" viewBox="0 0 1200 70" aria-hidden="true">
    <path d="M0 8 C 150 55, 330 65, 560 45 C 800 25, 1000 0, 1200 18 L1200 70 L0 70 Z" fill="#ffffff"/>
  </svg>
</section>
<h2 class="section-heading" style="top:1310px"><span>Our Mission</span></h2>
<p class="mission-text">At <em>RTM</em>, we are committed to reshaping the future of farming through <em>regenerative agriculture</em>. Our solutions go beyond sustainability, actively restoring ecosystems and improving soil health while delivering superior yields. With water-efficient irrigation, innovative agronomy, and a deep focus on soil vitality, we empower farmers to grow more sustainably and profitably.</p>

<div class="why-photo" role="img" aria-label="Farmer's hands letting seeds fall onto a field"></div>
<section class="why-box">
  <h2 class="why-title">Why choose us?</h2>
  <ol class="why-list">
    <li class="why-item" style="top:104px"><span class="num">1.</span><strong>Champions of Regenerative Agriculture:</strong> We don't just sustain—we regenerate, creating long-term benefits for the environment and your farm.</li>
    <li class="why-item" style="top:211px"><span class="num">2.</span><strong>Cutting-Edge Innovation:</strong> Access the latest technologies that promote ecosystem restoration and climate resilience.</li>
    <li class="why-item" style="top:316px"><span class="num">3.</span><strong>Global Expertise:</strong> Decades of experience bringing sustainable solutions to diverse farming environments worldwide.</li>
    <li class="why-item" style="top:420px"><span class="num">4.</span><strong>Tailored for Your Success:</strong> We work with you to create strategies that meet the unique needs of your farm and community.</li>
  </ol>
</section>

<section class="impact" role="img" aria-label="Golden wheat field background">
  <h2 class="impact-title">Our Impact</h2>
  <p class="impact-text">We are proud to help farmers build resilient farms, sequester carbon, and regenerate the land. Our approach ensures healthy soils, vibrant ecosystems, and productive crops for generations to come.</p>
</section>

<footer class="site-footer">
  <p class="copyright">© Copyright RTM Global 2024</p>
  <span class="social" style="left:979px"></span>
  <span class="social" style="left:1022px"></span>
</footer>

</body>
</html>
```